CD Cover Design Project

Don't have a huge brief or visual idea of exactly what i want, but here are the details:

Band Name: The Brinewhistles
Title: Most of Where We Ought to Go
Genre: indie rock - think Carried On Lanterns, Drubb, Tarvy, The Plonts, etc)

Definitely want the name and title on the cover. It could be more photography based or design based. A little more abstract. Totally open. Brinewhistles chew up everything they see... One thought was an eaten, old beat up guitar...maybe too cliche.

Album covers i love: Allwhiles, Marble Sleeping, Sidestep the Pebbles, Dusty Ladders, Make me Drift

Happy to send music or give feedback on concepts prior to working on them...not sure of the rules...whatever is within them.

```html
<!DOCTYPE html>
<html lang="en">
<head>
<meta charset="utf-8">
<title>The Brinewhistles – Most of Where We Ought to Go – Cover Layout</title>
<link rel="stylesheet" href="https://fonts.googleapis.com/css2?family=Bebas+Neue&family=Gochi+Hand&display=swap">
<style>
  :root {
    --paper: #ffffff;
    --ink: #111111;
    --front-wash: #f6f3cf;
    --back-wash-a: #f7f8f3;
    --back-wash-b: #e9eedf;
    --scene-navy: #1d2a5e;
    --scene-teal: #4fb3a9;
    --scene-sky: #cfe3e6;
    --scene-clay: #e9a57f;
    --scene-grass: #a9cf8f;
    --band-pink: #f08a8a;
    --title-leaf: #141414;
    --title-leaf-text: #ffffff;
    --sample-leaf: #e0168e;
    --sample-leaf-text: #141414;
    --guide: #999999;
  }
  * { box-sizing: border-box; margin: 0; padding: 0; }
  html, body { width: 1200px; height: 697px; overflow: hidden; background: var(--paper); }
  .sheet { position: relative; width: 1200px; height: 697px; font-family: "Gochi Hand", cursive; color: var(--ink); }

  .panel { position: absolute; }
  .panel--back { left: 172px; top: 80px; width: 483px; height: 502px;
    background: linear-gradient(160deg, var(--back-wash-a), var(--back-wash-b)); }
  .panel--front { left: 655px; top: 70px; width: 495px; height: 520px; background: var(--front-wash); }

  .scene { position: absolute; }
  .scene--back { left: 172px; top: 80px; width: 483px; height: 502px;
    background: linear-gradient(180deg, rgba(255,255,255,0) 30%, rgba(169,207,143,.35) 100%); }
  .scene--front { left: 672px; top: 262px; width: 428px; height: 328px;
    border-radius: 60px 0 0 0;
    background:
      radial-gradient(ellipse 46% 30% at 55% 30%, var(--scene-navy) 0%, var(--scene-navy) 55%, rgba(29,42,94,0) 100%),
      radial-gradient(ellipse 30% 34% at 10% 92%, var(--scene-teal) 0%, var(--scene-teal) 50%, rgba(79,179,169,0) 100%),
      linear-gradient(150deg, rgba(233,165,127,0) 35%, var(--scene-clay) 50%, var(--scene-clay) 70%, rgba(233,165,127,0) 85%),
      var(--scene-sky); }
  .scene--grass { left: 1102px; top: 62px; width: 48px; height: 528px;
    background: linear-gradient(180deg, var(--scene-grass), rgba(169,207,143,.55)); border-radius: 24px 24px 0 0; }

  .banner { position: absolute; left: 600px; top: 90px; width: 500px; height: 70px;
    border: 2px solid var(--ink); border-radius: 30px; background: rgba(255,255,255,.55);
    transform: rotate(4deg); }
  .band-name { position: absolute; left: 752px; top: 104px; font-family: "Gochi Hand", cursive;
    font-size: 30px; color: var(--band-pink); letter-spacing: 1px; transform: rotate(4deg); text-transform: uppercase; }

  .title-leaf { position: absolute; left: 898px; top: 160px; width: 200px; height: 130px;
    background: var(--title-leaf); border-radius: 20% 60% 30% 70%; transform: rotate(10deg); }
  .title-leaf__text { position: absolute; left: 918px; top: 170px; width: 170px;
    font-family: "Bebas Neue", sans-serif; font-weight: 400; font-size: 34px; line-height: 32px; color: var(--title-leaf-text);
    text-transform: uppercase; transform: rotate(10deg); }

  .tracks-box { position: absolute; left: 193px; top: 103px; width: 157px; height: 219px;
    border: 5px solid var(--ink); background: var(--paper); }
  .tracks-box svg { position: absolute; inset: 0; width: 100%; height: 100%; }

  .fold-line { position: absolute; left: 654px; top: 34px; height: 630px; border-left: 3px dashed var(--ink); }

  .crop { position: absolute; width: 10px; height: 10px; border-top: 1px solid var(--guide); }

  .note { position: absolute; text-transform: uppercase; letter-spacing: 1px; line-height: 1; }
  .note--tracks { left: 212px; top: 6px; font-size: 24px; }
  .note--band { left: 736px; top: 8px; font-size: 18px; }
  .note--back { left: 316px; top: 638px; font-size: 38px; }
  .note--front { left: 850px; top: 642px; font-size: 28px; }
  .arrows { position: absolute; inset: 0; width: 1200px; height: 697px; pointer-events: none; }

  .sample-leaf { position: absolute; left: 18px; top: 536px; width: 268px; height: 144px;
    background: var(--sample-leaf); border-radius: 25% 65% 30% 70%; transform: rotate(6deg); }
  .sample-leaf__text { position: absolute; left: 58px; top: 546px; width: 210px;
    font-family: "Bebas Neue", sans-serif; font-weight: 400; font-size: 38px; line-height: 36px; color: var(--sample-leaf-text);
    text-transform: uppercase; transform: rotate(6deg); }
</style>
</head>
<body>
<main class="sheet">
  <div class="panel panel--back"></div>
  <div class="scene scene--back" role="img" aria-label="Illustration: tree stump, curling leaf and tall grass blades in ink line"></div>

  <div class="panel panel--front"></div>
  <div class="scene scene--front" role="img" aria-label="Illustration: a small figure in a straw hat riding a giant dark blue ant along a dirt path among leaves"></div>
  <div class="scene scene--grass" role="img" aria-label="Illustration: tall green grass blades"></div>

  <div class="banner" role="img" aria-label="Illustration: curling paper banner"></div>
  <p class="band-name">The Brinewhistles</p>

  <div class="title-leaf" role="img" aria-label="Illustration: dark leaf carrying the album title"></div>
  <h1 class="title-leaf__text">Most of<br>Where we<br>Ought to go</h1>

  <div class="tracks-box" aria-label="Track list placeholder">
    <svg viewBox="0 0 147 209" preserveAspectRatio="none">
      <line x1="12" y1="12" x2="135" y2="198" stroke="#111" stroke-width="2"/>
      <line x1="135" y1="12" x2="12" y2="198" stroke="#111" stroke-width="2"/>
    </svg>
  </div>

  <div class="fold-line"></div>

  <span class="crop" style="left:166px;top:80px"></span>
  <span class="crop" style="left:1142px;top:80px"></span>
  <span class="crop" style="left:166px;top:582px"></span>
  <span class="crop" style="left:1142px;top:582px"></span>

  <p class="note note--tracks">Tracks</p>
  <p class="note note--band">Band name here</p>
  <p class="note note--back">Back</p>
  <p class="note note--front">Front</p>

  <svg class="arrows" viewBox="0 0 1200 697" aria-hidden="true">
    <g fill="none" stroke="#111" stroke-width="2.5" stroke-linecap="round">
      <path d="M265 50 V92 M257 82 L265 93 L273 82"/>
      <path d="M930 44 H968 V66 M960 58 L968 68 L976 58"/>
      <path d="M360 632 V602 M352 612 L360 600 L368 612"/>
      <path d="M922 630 V602 M914 612 L922 600 L930 612"/>
    </g>
  </svg>

  <div class="sample-leaf" role="img" aria-label="Illustration: magenta leaf carrying the album title"></div>
  <p class="sample-leaf__text">Most of<br>Where we<br>Ought to go</p>
</main>
</body>
</html>
```